Email Signature and a letter head

I need a professional email signature and a letter head for letters sent by post. I've attached my logo and a signature i am currently using. Current letter head is also attached.

Target Market(s)

Accounting Clients

Industry/Entity Type

Public Accounting

Font styles to use
Sans Serif

Colors

Designer to choose colors to be used in the design.

Requirements
Must have
• My logo, PW Logo, Blumo Logo, Tax Agent logo. All attached.
• All my credentials - examples in the attached documents

```html
<!DOCTYPE html>
<html lang="en">
<head>
<meta charset="utf-8">
<title>Keystone Ledger Advisory – Letterhead and Email Signature</title>
<link rel="stylesheet" href="https://fonts.googleapis.com/css2?family=Lora:wght@400;500&family=Open+Sans:wght@400;600&display=swap">
<style>
  :root{
    --backdrop:#b3b3b3;
    --paper:#f7f7f7;
    --gold:#a8892a;
    --gold-soft:#e9e9e9;
    --ink:#333333;
    --band-dark:#333333;
    --badge-grey:#cfcfcf;
    --legal-blue:#3c4f8c;
    --eco-green:#3f9a3a;
    --white:#ffffff;
  }
  *{box-sizing:border-box;margin:0;padding:0}
  html,body{width:1200px;height:872px;overflow:hidden}
  body{background:var(--backdrop);position:relative;font-family:"Lora",Georgia,serif;color:var(--ink)}
  .abs{position:absolute}

  /* Letterhead */
  .letterhead{left:182px;top:145px;width:411px;height:582px;background:var(--paper);overflow:hidden}
  .letterhead .brand-mark{left:178px;top:22px;width:56px;height:56px;border:2px solid var(--gold);border-radius:50%}
  .brand-name{text-align:center;color:var(--gold);font-weight:400;line-height:1.15}
  .brand-name .sub{display:block;letter-spacing:2px}
  .letterhead .brand-name{left:0;width:411px;top:84px;font-size:13px;letter-spacing:0.5px}
  .letterhead .brand-name .sub{font-size:6px}
  .letterhead .watermark{left:59px;top:151px;width:294px;height:294px;border:4px solid var(--gold-soft);border-radius:50%}
  .sender-name{left:20px;top:526px;color:var(--gold);font-size:13px;font-weight:500;white-space:nowrap}
  .sender-lines{left:20px;top:544px;font-size:7.4px;line-height:9px;white-space:nowrap}
  .sender-lines .ids{color:var(--gold);padding-left:10px}
  .ico{display:inline-block;width:7px;height:7px;vertical-align:-1px;margin-right:2px}

  .partner-dot{border-radius:50%;background:var(--badge-grey)}
  .partner-word{color:var(--ink);font-family:"Lora",Georgia,serif;font-weight:400;white-space:nowrap}
  .letterhead .partner-word{left:240px;top:532px;font-size:10px;line-height:18px}
  .letterhead .partner-blumo-dot{left:272px;top:529px;width:24px;height:24px}
  .letterhead .partner-pw{left:308px;top:530px;width:22px;height:22px}
  .letterhead .partner-tax{left:344px;top:530px;width:24px;height:24px}
  .tax-label{font-family:"Open Sans",Arial,sans-serif;font-weight:600;color:var(--ink);white-space:nowrap}
  .letterhead .tax-label{left:373px;top:536px;font-size:5px;line-height:6px}
  .letterhead .foot-band{left:0;top:576px;width:411px;height:6px;background:var(--band-dark)}
  .letterhead .foot-web{left:238px;top:564px;width:173px;height:18px;background:var(--gold);clip-path:polygon(5px 0,100% 0,100% 100%,0 100%);color:var(--white);font-size:7px;line-height:18px;text-align:right;padding-right:16px}

  /* Email signature */
  .signature{left:633px;top:423px;width:370px;height:90px;background:var(--white);border:1px solid #d7d7d7;overflow:hidden}
  .signature .brand-mark{left:37px;top:14px;width:38px;height:38px;border:1.5px solid var(--gold);border-radius:50%}
  .signature .brand-name{left:0;width:113px;top:56px;font-size:7.5px}
  .signature .brand-name .sub{font-size:4px;letter-spacing:1.2px}
  .signature .divider{left:147px;top:14px;width:1.5px;height:52px;background:var(--gold)}
  .signature .sender-name{left:158px;top:13px;font-size:10px}
  .signature .sender-ids{left:158px;top:26px;font-size:5.6px;color:var(--gold);white-space:nowrap}
  .signature .sender-lines{left:158px;top:36px;font-size:5.6px;line-height:7.2px}
  .signature .ico{width:5px;height:5px}
  .signature .partner-word{left:318px;top:17px;font-size:7px;line-height:12px}
  .signature .partner-blumo-dot{left:341px;top:16px;width:14px;height:14px}
  .signature .partner-pw{left:334px;top:37px;width:13px;height:13px}
  .signature .partner-tax{left:322px;top:62px;width:15px;height:15px}
  .signature .tax-label{left:340px;top:65px;font-size:3.8px;line-height:4.6px}
  .signature .foot-band{left:0;top:83px;width:370px;height:7px;background:var(--band-dark)}
  .signature .tagline{left:0;top:78px;width:134px;height:12px;background:var(--gold);clip-path:polygon(0 0,126px 0,100% 100%,0 100%);color:var(--white);font-family:"Open Sans",Arial,sans-serif;font-size:5.2px;line-height:12px;padding-left:12px}
  .legal{left:635px;top:518px;width:365px;font-family:"Open Sans",Arial,sans-serif;font-size:5px;line-height:7px;color:var(--legal-blue)}
  .eco{left:644px;top:543px;display:flex;align-items:center;gap:14px;font-family:"Open Sans",Arial,sans-serif;font-size:5.2px;color:var(--eco-green)}
</style>
</head>
<body>

<section class="abs letterhead" aria-label="Letterhead">
  <div class="abs brand-mark"></div>
  <div class="abs brand-name">KEYSTONE LEDGER<span class="sub">ADVISORY</span></div>
  <div class="abs watermark"></div>

  <div class="abs sender-name">Marlise Crane PW BBus.</div>
  <div class="abs sender-lines">
    <div><svg class="ico" viewBox="0 0 10 10"><path d="M2 1h2l1 2-1.3 1a6 6 0 0 0 2.3 2.3L7 5l2 1v2c-4 1-8-3-7-7z" fill="var(--ink)"/></svg>0400 217 845 &nbsp;<svg class="ico" viewBox="0 0 10 10"><rect x="0.5" y="2" width="9" height="6" fill="var(--ink)"/><path d="M0.5 2 5 5.5 9.5 2" stroke="var(--paper)" fill="none"/></svg>marlise@keystoneledger.example</div>
    <div><svg class="ico" viewBox="0 0 10 10"><path d="M5 0a3.5 3.5 0 0 0-3.5 3.5C1.5 6 5 10 5 10s3.5-4 3.5-6.5A3.5 3.5 0 0 0 5 0zm0 5a1.5 1.5 0 1 1 0-3 1.5 1.5 0 0 1 0 3z" fill="var(--gold)"/></svg>18 Harbour Lane Seacliff VIC 3990</div>
    <div class="ids">ABN: 41 203 776 518 &nbsp;| &nbsp;TAN: 318 442 07</div>
  </div>

  <div class="abs partner-word">Blumo</div>
  <div class="abs partner-dot partner-blumo-dot"></div>
  <div class="abs partner-dot partner-pw"></div>
  <div class="abs partner-dot partner-tax"></div>
  <div class="abs tax-label">Tax Agent<br>31844207</div>

  <div class="abs foot-band"></div>
  <div class="abs foot-web">www.keystoneledger.example</div>
</section>

<section class="abs signature" aria-label="Email signature">
  <div class="abs brand-mark"></div>
  <div class="abs brand-name">KEYSTONE LEDGER<span class="sub">ADVISORY</span></div>
  <div class="abs divider"></div>

  <div class="abs sender-name">Marlise Crane PW BBus.</div>
  <div class="abs sender-ids">ABN: 41 203 776 518 &nbsp;| &nbsp;TAN: 318 442 07</div>
  <div class="abs sender-lines">
    <div><svg class="ico" viewBox="0 0 10 10"><path d="M2 1h2l1 2-1.3 1a6 6 0 0 0 2.3 2.3L7 5l2 1v2c-4 1-8-3-7-7z" fill="var(--ink)"/></svg>0400 217 845</div>
    <div><svg class="ico" viewBox="0 0 10 10"><circle cx="5" cy="5" r="4" fill="none" stroke="var(--ink)"/></svg>www.keystoneledger.example</div>
    <div><svg class="ico" viewBox="0 0 10 10"><rect x="0.5" y="2" width="9" height="6" fill="var(--ink)"/></svg>marlise@keystoneledger.example</div>
    <div><svg class="ico" viewBox="0 0 10 10"><path d="M5 0a3.5 3.5 0 0 0-3.5 3.5C1.5 6 5 10 5 10s3.5-4 3.5-6.5A3.5 3.5 0 0 0 5 0z" fill="var(--gold)"/></svg>18 Harbour Lane Seacliff VIC 3990</div>
  </div>

  <div class="abs partner-word">Blumo</div>
  <div class="abs partner-dot partner-blumo-dot"></div>
  <div class="abs partner-dot partner-pw"></div>
  <div class="abs partner-dot partner-tax"></div>
  <div class="abs tax-label">Tax Agent<br>31844207</div>

  <div class="abs foot-band"></div>
  <div class="abs tagline">Balance is the key of everything in life</div>
</section>

<p class="abs legal">This e-mail and its attachments are confidential and privileged. Any unauthorised use is expressly prohibited. If you receive this e-mail in error please contact us, then delete the e-mail.</p>

<div class="abs eco">
  <svg width="14" height="12" viewBox="0 0 14 12" aria-hidden="true"><path d="M7 0 3 5h2.5L2 9h10L8.5 5H11z" fill="var(--eco-green)"/><rect x="6" y="9" width="2" height="3" fill="var(--eco-green)"/></svg>
  <span>Please consider the environment before printing this e-mail notice.</span>
</div>

</body>
</html>
```